Business Card Design To Look Just Like a Credit Card- Needed

I would like to take my new Logo just designed here at Pixel Harbor and make a new business card and template for future additional sales people.
The credit card should have an eye catching design but look real. I have seen some that have similar logos to LORU or TrustPlaque too. However,it must have a smart chip design in it too. Make sure it has a black fake magnetic strip and other characteristics of an actual modern credit card.
This may be printed on paper and blank plastic cards.

Most the information will be on the back but the name will be on front with the logo, phone number.

Must Have Info:
Leonard Whitfield
President

2964 Maple Hollow Rd, Bldg 417
Fairport, NY 14582
252-555-0187
leonard@brightledgerco.net
Updates

Phone number is 585 area code not 252! my bad

also, please add website address www.brightledgerco.net
Thanks,

LW

Industry/Entity Type

Credit Card

Requirements
Must have
• My Logo, smart chip, fake magnetic strip

```html
<!DOCTYPE html>
<html lang="en">
<head>
<meta charset="utf-8">
<title>Bright Ledger – Credit Card Style Business Card</title>
<link rel="stylesheet" href="https://fonts.googleapis.com/css2?family=Questrial&display=swap">
<style>
  :root {
    --page-bg: #2a2522;
    --card-dark: #1c1c1e;
    --card-mid: #5a5a5e;
    --card-light: #b9babd;
    --brand-green: #0f7a35;
    --text-light: #e3e3e3;
    --text-muted: #a9a9ab;
    --rule: #8c8c8e;
    --chip-gold: #c89a3a;
    --chip-gold-light: #ecd08a;
    --stripe: #060606;
    --holo: #efeee8;
  }
  * { margin: 0; padding: 0; box-sizing: border-box; }
  html, body {
    width: 1200px; height: 900px; overflow: hidden;
    background: var(--page-bg);
    font-family: "Questrial", "Century Gothic", sans-serif;
  }
  .canvas { position: relative; width: 1200px; height: 900px; }

  .card {
    position: absolute;
    width: 560px; height: 352px;
    border-radius: 22px;
    overflow: hidden;
    box-shadow: 0 10px 30px rgba(0,0,0,.45);
  }

  /* Front */
  .card-front {
    left: 70px; top: 80px;
    background: radial-gradient(ellipse at 55% 55%, var(--card-light) 0%, var(--card-mid) 55%, var(--card-dark) 100%);
  }
  .world-map {
    position: absolute; left: 40px; top: 30px; width: 480px; height: 250px;
    background: radial-gradient(ellipse at 50% 50%, rgba(20,20,22,.55), rgba(20,20,22,.15) 70%, transparent 100%);
    border-radius: 40%;
  }
  .chip {
    position: absolute; left: 70px; top: 190px; width: 62px; height: 48px;
    border-radius: 8px;
    background: linear-gradient(135deg, var(--chip-gold-light), var(--chip-gold) 60%, #8c6a22);
  }
  .hologram {
    position: absolute; right: 52px; top: 44px; width: 78px; height: 62px;
    border-radius: 9px;
    background: linear-gradient(135deg, #fbfaf4, var(--holo) 60%, #d9d6c8);
  }
  .front-brand {
    position: absolute; left: 170px; top: 150px;
    display: flex; align-items: center; gap: 14px;
  }
  .brand-mark {
    width: 26px; height: 26px; border-radius: 50%;
    background: var(--brand-green);
    flex: none;
  }
  .brand-name {
    color: var(--brand-green);
    font-size: 46px; line-height: 1; letter-spacing: 1px;
    text-transform: uppercase;
    white-space: nowrap;
  }
  .brand-name .brand-line { display: block; }

  /* Back */
  .card-back {
    left: 570px; top: 470px;
    background: linear-gradient(160deg, #6a6a6c 0%, #3a3a3c 45%, #222224 100%);
  }
  .back-brand {
    position: absolute; right: 34px; top: 30px;
    display: flex; align-items: center; gap: 8px;
  }
  .back-brand .brand-mark { width: 14px; height: 14px; }
  .back-brand .brand-name { font-size: 24px; }

  .holder { position: absolute; left: 40px; top: 92px; }
  .holder-name { color: var(--text-light); font-size: 19px; }
  .holder-title { color: var(--text-muted); font-size: 12px; margin-top: 3px; }

  .contact-block {
    position: absolute;
    border-left: 1px solid var(--rule);
    padding-left: 14px;
    color: var(--text-light);
  }
  .contact-left { left: 40px; top: 150px; }
  .contact-right { left: 300px; top: 92px; color: var(--text-muted); }
  .contact-line {
    display: flex; align-items: center; gap: 10px;
    font-size: 15px; line-height: 24px;
    white-space: nowrap;
  }
  .contact-right .contact-line { font-size: 14px; line-height: 20px; align-items: flex-start; }
  .icon { width: 12px; height: 12px; flex: none; fill: var(--text-muted); }

  .mag-stripe {
    position: absolute; left: 0; right: 0; top: 236px; height: 50px;
    background: var(--stripe);
  }
</style>
</head>
<body>
<main class="canvas">

  <section class="card card-front" aria-label="Card front">
    <div class="world-map" role="img" aria-label="Striped world map background"></div>
    <div class="chip" role="img" aria-label="Gold smart chip"></div>
    <div class="hologram" role="img" aria-label="Hologram with bird emblem"></div>
    <div class="front-brand">
      <span class="brand-mark"></span>
      <span class="brand-name"><span class="brand-line">Bright</span><span class="brand-line">Ledger</span></span>
    </div>
  </section>

  <section class="card card-back" aria-label="Card back">
    <div class="back-brand">
      <span class="brand-mark"></span>
      <span class="brand-name">Bright Ledger</span>
    </div>

    <div class="holder">
      <p class="holder-name">Leonard Whitfield</p>
      <p class="holder-title">President</p>
    </div>

    <div class="contact-block contact-right">
      <p class="contact-line">
        <svg class="icon" viewBox="0 0 12 12"><path d="M6 0a4 4 0 0 0-4 4c0 3 4 8 4 8s4-5 4-8a4 4 0 0 0-4-4zm0 5.5A1.5 1.5 0 1 1 6 2.5a1.5 1.5 0 0 1 0 3z"/></svg>
        <span>2964 Maple Hollow Rd, Bldg 417<br>Fairport, NY 14582</span>
      </p>
    </div>

    <div class="contact-block contact-left">
      <p class="contact-line">
        <svg class="icon" viewBox="0 0 12 12"><path d="M2.5 0.5l2 2-1.2 1.6c.7 1.6 1.9 2.8 3.6 3.6L8.5 6.5l2 2-1.5 2.5C4.5 10.5 1 7 .5 2z"/></svg>
        <span>585-555-0187</span>
      </p>
      <p class="contact-line">
        <svg class="icon" viewBox="0 0 12 12"><circle cx="6" cy="6" r="5" fill="none" stroke="#a9a9ab" stroke-width="1.4"/><circle cx="6" cy="6" r="2" fill="none" stroke="#a9a9ab" stroke-width="1.4"/></svg>
        <span>leonard@brightledgerco.net</span>
      </p>
      <p class="contact-line">
        <svg class="icon" viewBox="0 0 12 12"><g fill="none" stroke="#a9a9ab" stroke-width="1.1"><circle cx="6" cy="6" r="5"/><ellipse cx="6" cy="6" rx="2.2" ry="5"/><path d="M1 6h10"/></g></svg>
        <span>www.brightledgerco.net</span>
      </p>
    </div>

    <div class="mag-stripe" role="img" aria-label="Magnetic stripe"></div>
  </section>

</main>
</body>
</html>
```